Professional Modern Website Design

We are a premium IT services provider to the financial industry based in London. Our company is called Veltra our current holding page is www.veltra-example.co.uk. We require a new website to match our new corporate identity. This project is for the design phase only. Development will be handled in-house. I have attached examples of wire frames we have developed (although open to suggestions for improvement) Our brand document that should demonstrate current brand, inc how we communicate to potential clients and finally mostly completed web-content.
We are looking for designers that can create something that sets us apart from our competitors.
Target Market(s)
IT Decision makers in Finance companies such as; hedge funds, private investment banks etc
Industry/Entity Type
Financial
Number of Pages Required
5+ page
Requirements
Must have
- hexagon elements in the design, unique design.
Nice to have
- Blog and social media feeds
Should not have
- Should not resemble a downloaded template

```html
<!DOCTYPE html>
<html lang="en">
<head>
<meta charset="utf-8">
<title>Veltra — IT Services for Finance</title>
<link href="https://fonts.googleapis.com/css2?family=Source+Sans+3:wght@400;600;700&display=swap" rel="stylesheet">
<style>
:root{
  --orange:#f07125;
  --orange-dark:#d85f17;
  --ink:#222222;
  --text:#3a3a3a;
  --white:#ffffff;
  --footer:#2b2b2b;
  --footer-bottom:#1d1d1d;
  --footer-text:#e4e4e4;
  --field-line:#5a5a5a;
}
*{margin:0;padding:0;box-sizing:border-box}
html,body{width:1200px;height:2395px;overflow:hidden}
body{font-family:"Source Sans 3",sans-serif;color:var(--text);background:var(--white);position:relative}
section,header,footer{position:absolute;left:0;width:1200px}

/* Hero */
.hero{top:0;height:591px;overflow:hidden}
.hero-photo{position:absolute;inset:0;background:linear-gradient(120deg,#3b4046 0%,#5a5f63 45%,#34383d 100%)}
.hero-shade{position:absolute;inset:0;background:rgba(30,32,36,.55)}
.brand{position:absolute;top:30px;left:0;width:1200px;display:flex;justify-content:center;align-items:center;gap:10px}
.brand-mark{width:22px;height:22px;background:var(--orange)}
.brand-name{font-size:34px;font-weight:700;color:var(--orange);letter-spacing:1px}
.nav{position:absolute;top:138px;left:0;width:1200px;height:40px}
.nav a{position:absolute;top:0;height:40px;line-height:40px;font-size:14px;font-weight:600;color:var(--orange);text-decoration:none;letter-spacing:.5px}
.nav a.active{border:1.5px solid var(--orange);padding:0 18px}
.about-title{position:absolute;left:82px;top:296px;font-size:20px;font-weight:600;color:var(--orange);letter-spacing:.5px}
.about-text{position:absolute;left:82px;top:340px;width:660px;font-size:13px;line-height:21px;font-weight:600;color:var(--white)}

/* Shared section heading */
.section-title{position:absolute;left:0;width:1200px;text-align:center;font-size:20px;font-weight:700;color:var(--orange);letter-spacing:.5px}
.section-intro{position:absolute;left:120px;width:960px;text-align:center;font-size:13px;line-height:20px;color:var(--ink)}

/* Values */
.values{top:591px;height:540px}
.value{position:absolute;top:157px;width:300px;text-align:center}
.value svg{display:block;margin:0 auto;width:226px;height:216px}
.value-name{margin-top:22px;font-size:15px;font-weight:700;color:var(--orange)}
.value-text{margin-top:12px;font-size:13px;line-height:17px;color:var(--ink);padding:0 20px}

/* People */
.people{top:1131px;height:474px;overflow:hidden}
.people-photo{position:absolute;inset:0;background:linear-gradient(100deg,#3f4348 0%,#6d7276 50%,#9ea3a6 100%)}
.people-shade{position:absolute;inset:0;background:rgba(25,27,30,.35)}
.people-card{position:absolute;left:82px;top:48px;width:549px;height:372px;background:rgba(216,95,23,.88);padding:50px 40px 0}
.people-card h2{text-align:center;font-size:20px;font-weight:700;color:var(--white);letter-spacing:.5px}
.people-card p{margin-top:16px;font-size:12.5px;line-height:17.5px;font-weight:600;color:var(--white)}

/* Awards */
.awards{top:1605px;height:385px}
.award{position:absolute;top:165px;width:150px;height:172px}

/* Footer */
.footer{top:1990px;height:341px;background:var(--footer)}
.col-title{position:absolute;top:48px;font-size:14px;font-weight:600;color:var(--orange);letter-spacing:.3px}
.link-list{position:absolute;top:95px;left:82px;list-style:none;font-size:12px;line-height:23px;color:var(--footer-text)}
.footer-text{position:absolute;top:92px;left:258px;width:320px;font-size:12px;line-height:19px;color:var(--footer-text)}
.post{position:absolute;left:625px;width:240px;font-size:12px;line-height:18px;color:var(--footer-text)}
.post time{display:block;color:var(--orange);font-weight:700}
.field{position:absolute;border:1px solid var(--field-line);font-size:12px;color:#cfcfcf;padding:7px 10px}
.send{position:absolute;left:897px;top:245px;width:103px;height:35px;background:var(--orange);color:var(--white);font-size:13px;font-weight:700;text-align:center;line-height:35px}

/* Bottom bar */
.bottom{position:absolute;left:0;top:2331px;width:1200px;height:64px;background:var(--footer-bottom)}
.copyright{position:absolute;top:0;left:0;width:1200px;text-align:center;line-height:64px;font-size:13px;font-weight:600;color:var(--white)}
.social{position:absolute;right:77px;top:22px;display:flex;gap:10px}
.social span{width:18px;height:18px;border-radius:50%;background:var(--white)}
.social span:last-child{background:var(--orange);border-radius:3px}
</style>
</head>
<body>

<header class="hero">
  <div class="hero-photo" role="img" aria-label="Photo of a modern office with colleagues working at desks"></div>
  <div class="hero-shade"></div>
  <div class="brand"><span class="brand-mark"></span><span class="brand-name">Veltra</span></div>
  <nav class="nav">
    <a style="left:296px">ABOUT</a>
    <a style="left:413px">SERVICES</a>
    <a class="active" style="left:553px">PARTNERS</a>
    <a style="left:727px">CLIENTS</a>
    <a style="left:845px">CONTACT</a>
  </nav>
  <h1 class="about-title">ABOUT VELTRA</h1>
  <p class="about-text">Lorem ipsum dolor sit amet, consectetur adipisicing elit, sed do eiusmod tempor incididunt ut labore et dolore magna aliqua. Ut enim ad minim veniam, quis nostrud exercitation ullamco laboris nisi ut aliquip ex ea commodo consequat. Duis aute irure dolor in reprehenderit in voluptate velit esse cillum dolore eu fugiat nulla pariatur. Excepteur sint occaecat cupidatat non proident, sunt in culpa qui officia deserunt mollit anim id est la</p>
</header>

<section class="values">
  <h2 class="section-title" style="top:50px">OUR VALUES</h2>
  <p class="section-intro" style="top:83px">orem ipsum dolor sit amet, consectetur adipisicing elit, sed do eiusmod tempor incididunt ut labore et dolore magna aliqua. Ut enim ad minim veniam, quis nostrud exercitation ullamco laboris nisi ut aliquip ex ea commodo consequat. Duis aute irure dolor in reprehenderit in voluptate velit esse cillum dolore eu</p>

  <div class="value" style="left:132px">
    <svg viewBox="0 0 100 100" aria-hidden="true"><polygon points="50,3 95,27 95,73 50,97 5,73 5,27" fill="var(--orange)" stroke="var(--orange)" stroke-width="4" stroke-linejoin="round"/>
      <path d="M34 51 L45 62 L67 39" fill="none" stroke="var(--white)" stroke-width="4" stroke-linecap="round" stroke-linejoin="round"/></svg>
    <div class="value-name">COMMITMENT</div>
    <p class="value-text">orem ipsum dolor sit amet, consectetur adipisicing elit, sed do eiusmod tempor incididunt ut labore et dolore magna aliqua. U</p>
  </div>
  <div class="value" style="left:470px">
    <svg viewBox="0 0 100 100" aria-hidden="true"><polygon points="50,3 95,27 95,73 50,97 5,73 5,27" fill="var(--orange)" stroke="var(--orange)" stroke-width="4" stroke-linejoin="round"/>
      <path d="M32 50 H66 M55 38 L67 50 L55 62" fill="none" stroke="var(--white)" stroke-width="4" stroke-linecap="round" stroke-linejoin="round"/></svg>
    <div class="value-name">DYNAMISM</div>
    <p class="value-text">orem ipsum dolor sit amet, consectetur adipisicing elit, sed do eiusmod tempor incididunt ut labore et dolore magna aliqua. U</p>
  </div>
  <div class="value" style="left:803px">
    <svg viewBox="0 0 100 100" aria-hidden="true"><polygon points="50,3 95,27 95,73 50,97 5,73 5,27" fill="var(--orange)" stroke="var(--orange)" stroke-width="4" stroke-linejoin="round"/>
      <path d="M34 42 H64 M56 34 L64 42 L56 50 M66 58 H36 M44 50 L36 58 L44 66" fill="none" stroke="var(--white)" stroke-width="4" stroke-linecap="round" stroke-linejoin="round"/></svg>
    <div class="value-name">AGILITY</div>
    <p class="value-text">orem ipsum dolor sit amet, consectetur adipisicing elit, sed do eiusmod tempor incididunt ut labore et dolore magna aliqua. U</p>
  </div>
</section>

<section class="people">
  <div class="people-photo" role="img" aria-label="Photo of two colleagues working at computers in an office"></div>
  <div class="people-shade"></div>
  <div class="people-card">
    <h2>OUR PEOPLE</h2>
    <p>Lorem ipsum dolor sit amet, consectetur adipisicing elit, sed do eiusmod tempor incididunt ut labore et dolore magna aliqua. Ut enim ad minim veniam, quis nostrud exercitation ullamco laboris nisi ut aliquip ex ea commodo consequat. Duis aute irure dolor in reprehenderit in voluptate velit esse cillum dolore eu fugiat nulla pariatur. Excepteur sint occaecat cupidatat non proident, sunt in culpa qui officia deserunt mollit anim id est laborum. Sed ut perspiciatis unde omnis iste natus error sit voluptatem accusantium doloremque laudantium, totam rem aperiam, eaque ipsa quae ab illo inventore veritatis et quasi architecto beatae vitae dicta sunt explicabo. Nemo enim ipsam voluptatem quia voluptas sit aspernatur aut odit aut fugit, sed quia consequuntur magni dolores eos qui ratione voluptatem sequi nesciunt. Neque porro quisquam est, qui dolorem ipsum</p>
  </div>
</section>

<section class="awards">
  <h2 class="section-title" style="top:50px">AWARDS</h2>
  <p class="section-intro" style="top:80px">orem ipsum dolor sit amet, consectetur adipisicing elit, sed do eiusmod tempor incididunt ut labore et dolore magna aliqua. Ut enim ad minim veniam, quis nostrud exercitation ullamco laboris nisi ut aliquip ex ea commodo consequat. Duis aute irure dolor in reprehenderit in voluptate velit esse cillum dolore eu</p>

  <svg class="award" style="left:77px" viewBox="0 0 100 115" aria-hidden="true"><polygon points="50,3 96,29 96,86 50,112 4,86 4,29" fill="var(--orange)"/>
    <polygon points="50,30 74,43 74,72 50,85 26,72 26,43" fill="none" stroke="var(--white)" stroke-width="3"/></svg>
  <svg class="award" style="left:276px" viewBox="0 0 100 115" aria-hidden="true"><polygon points="50,3 96,29 96,86 50,112 4,86 4,29" fill="var(--orange)"/>
    <polygon points="50,30 74,43 74,72 50,85 26,72 26,43" fill="none" stroke="var(--white)" stroke-width="3"/></svg>
  <svg class="award" style="left:476px" viewBox="0 0 100 115" aria-hidden="true"><polygon points="50,3 96,29 96,86 50,112 4,86 4,29" fill="var(--orange)"/>
    <polygon points="50,30 74,43 74,72 50,85 26,72 26,43" fill="none" stroke="var(--white)" stroke-width="3"/></svg>
  <svg class="award" style="left:678px" viewBox="0 0 100 115" aria-hidden="true"><polygon points="50,3 96,29 96,86 50,112 4,86 4,29" fill="var(--orange)"/>
    <polygon points="50,30 74,43 74,72 50,85 26,72 26,43" fill="none" stroke="var(--white)" stroke-width="3"/></svg>
  <svg class="award" style="left:878px" viewBox="0 0 100 115" aria-hidden="true"><polygon points="50,3 96,29 96,86 50,112 4,86 4,29" fill="var(--orange)"/>
    <polygon points="50,30 74,43 74,72 50,85 26,72 26,43" fill="none" stroke="var(--white)" stroke-width="3"/></svg>
</section>

<footer class="footer">
  <h3 class="col-title" style="left:82px">DOLOR SIT AMET</h3>
  <ul class="link-list">
    <li>consectetur</li><li>adipisicing elit</li><li>dolor sit amet</li><li>consectetur,</li><li>adipisci v</li><li>elitdolor sit amet</li><li>consectetur,</li>
  </ul>

  <h3 class="col-title" style="left:258px">LOREM IPSUM DOLOR</h3>
  <p class="footer-text">consectetur adipisicing elit, sed do eiusmod tempor incididunt ut labore et dolore magna aliqua. Ut enim ad minim veniam, quis nostrud exercitation ullamco laboris nisi ut aliquip ex ea commodo consequat. Duis aute irure dolor in reprehenderit in voluptate ore magna aliqua. Ut enim ad minim veniam, quis nostrud exercitation ullamco laboris nisi ut aliquip ex ea commodo consequat</p>

  <h3 class="col-title" style="left:625px">RECENT BLOG POST</h3>
  <div class="post" style="top:92px">consectetur adipisicing elit, sed do eiusmod tempor incidi<time>12.05.2015</time></div>
  <div class="post" style="top:158px">Ut enim ad minim veniam, quis nostrud exercitation<time>10.05.2015</time></div>
  <div class="post" style="top:224px">ullamco laboris nisi ut aliquip ex ea commodo consequat.<time>1.4.2015</time></div>

  <h3 class="col-title" style="left:897px">CONTACT US</h3>
  <div class="field" style="left:897px;top:93px;width:98px;height:38px">First name</div>
  <div class="field" style="left:1003px;top:93px;width:115px;height:38px">Last name</div>
  <div class="field" style="left:897px;top:138px;width:221px;height:81px">message</div>
  <div class="send">SENT</div>
</footer>

<div class="bottom">
  <p class="copyright">All right reserved by @2015 Veltra</p>
  <div class="social" aria-label="Social links"><span></span><span></span><span></span><span></span></div>
</div>

</body>
</html>
```